TideMill Coatings website development for protective coatings manufacturer

We require a website for a new company which manufacturers protective coatings for automotive and industrial applications. We have a new logo which can be used and will be uploaded for inclusion on the website. There should be the following pages:
Home
About us
Products
Distribution
Contact us
There will be 10 products with downloadable pdf files TDS and MSDS.
Target Market(s)
Automotive and industrial coatings
Industry/Entity Type
Protective Coatings manufacturing
Coding
Coded - Design and coding required
Font styles to use
Sans Serif
Requirements
Must have
- Nice and clear images related to the target market

```html
<!DOCTYPE html>
<html lang="en">
<head>
<meta charset="utf-8">
<title>TideMill Coatings</title>
<link href="https://fonts.googleapis.com/css2?family=Montserrat:wght@400;500;600;700;800&family=Open+Sans:wght@400;600&display=swap" rel="stylesheet">
<style>
:root{
  --blue:#2c66b5;
  --blue-dark:#1f4f93;
  --navy:#0f1c2f;
  --ink:#1b2536;
  --muted:#6b7380;
  --line:#e3e7ee;
  --soft:#f2f4f8;
  --white:#ffffff;
}
*{margin:0;padding:0;box-sizing:border-box}
html,body{width:1200px;height:3904px;overflow:hidden}
body{font-family:"Open Sans",Arial,sans-serif;color:var(--ink);background:var(--white);position:relative}
h1,h2,h3,h4,.nav,.btn,.brand{font-family:"Montserrat",Arial,sans-serif}

/* header */
.site-header{position:absolute;top:0;left:0;width:1200px;height:96px;background:var(--white)}
.brand{position:absolute;left:44px;top:14px;display:flex;align-items:center;gap:10px;font-weight:800;font-size:22px;color:var(--navy);line-height:1.05}
.brand-mark{width:30px;height:30px;background:var(--blue)}
.topbar{position:absolute;right:0;top:0;height:34px;display:flex;align-items:center}
.topbar .info{display:flex;align-items:center;gap:8px;font-size:12px;color:var(--ink);padding:0 18px;height:34px}
.topbar .info svg{width:14px;height:14px}
.topbar .phone{font-weight:700;font-size:15px;color:var(--blue);font-family:"Montserrat",sans-serif}
.topbar .request{background:var(--blue-dark);color:#fff;height:34px;padding:0 34px;display:flex;align-items:center;font-family:"Montserrat",sans-serif;font-weight:600;font-size:13px}
.nav{position:absolute;top:50px;right:60px;display:flex;gap:46px;font-size:13px;font-weight:600;color:var(--ink)}
.nav a{color:inherit;text-decoration:none;padding-bottom:8px}
.nav a.active{color:var(--blue);border-bottom:2px solid var(--blue)}

/* hero */
.hero{position:absolute;top:96px;left:0;width:1200px;height:470px;background:linear-gradient(120deg,#2b3038 0%,#444b55 45%,#1c2129 100%)}
.hero-text{position:absolute;top:96px;left:0;width:1200px;text-align:center;color:#fff}
.hero-text .eyebrow{font-family:"Montserrat",sans-serif;font-size:14px;letter-spacing:2px;font-weight:500}
.hero-text h1{font-size:38px;font-weight:800;line-height:1.2;margin:10px auto 26px;width:820px;text-transform:uppercase}
.btn{display:inline-block;background:var(--blue);color:#fff;font-weight:600;font-size:12px;text-transform:uppercase;padding:12px 30px;border-radius:3px;text-decoration:none}
.hero-cut{position:absolute;top:440px;left:0}
.scroll-down{position:absolute;top:574px;left:578px;width:44px;height:44px}

/* section titles */
.section-title{position:absolute;left:0;width:1200px;text-align:center;font-size:30px;font-weight:800;text-transform:uppercase;color:var(--ink)}
.section-title span{color:var(--blue)}
.title-rule{position:absolute;left:570px;width:60px;height:3px;background:var(--blue)}
.intro{position:absolute;left:350px;width:500px;text-align:center;font-size:12px;line-height:1.6;color:var(--muted)}

/* products */
.product-grid{position:absolute;top:834px;left:190px;width:820px;display:grid;grid-template-columns:repeat(3,1fr);gap:44px 26px}
.product-card{height:330px;background:#fff;box-shadow:0 3px 14px rgba(20,30,50,.12);position:relative;text-align:center}
.product-media{height:170px;width:100%}
.product-icon{position:absolute;top:150px;left:50%;width:40px;height:40px;margin-left:-20px;background:var(--blue-dark);transform:rotate(45deg);border:3px solid #fff}
.product-card h3{margin-top:46px;font-size:14px;font-weight:700}
.product-card p{margin:10px 22px 0;font-size:11px;line-height:1.6;color:var(--muted)}
.view-all{position:absolute;top:1606px;left:526px;background:var(--blue-dark)}

/* about */
.about{position:absolute;top:1780px;left:0;width:1200px;height:464px;background:var(--soft)}
.about-media{position:absolute;top:0;left:0;width:585px;height:464px;background:linear-gradient(135deg,#7a4b2e 0%,#b86a35 35%,#4f5966 70%,#2e3a4a 100%)}
.about-text{position:absolute;left:655px;top:26px;width:500px}
.about-text .eyebrow{font-size:11px;letter-spacing:2px;color:var(--blue);font-family:"Montserrat",sans-serif;font-weight:600;text-transform:uppercase}
.about-text h2{font-size:30px;font-weight:800;line-height:1.15;text-transform:uppercase;margin:6px 0 20px}
.about-text h2 span{color:var(--blue)}
.about-text p{font-size:12px;line-height:1.7;color:var(--muted);margin-bottom:14px}

/* industries */
.industries{position:absolute;top:2262px;left:0;width:1200px;height:400px;background:var(--blue)}
.industries h2{position:absolute;top:68px;width:1200px;text-align:center;color:#fff;font-size:30px;font-weight:800;text-transform:uppercase}
.industries .rule{position:absolute;top:112px;left:570px;width:60px;height:3px;background:#fff}
.industries .lead{position:absolute;top:128px;left:320px;width:560px;text-align:center;color:#dbe6f6;font-size:12px;line-height:1.6}
.industry-row{position:absolute;top:196px;left:184px;display:flex;gap:26px}
.industry{width:148px;height:110px;background:#fff;border-radius:3px;text-align:center;padding-top:18px;font-family:"Montserrat",sans-serif;font-size:12px;font-weight:600;color:var(--ink);line-height:1.3;position:relative}
.industry svg{width:34px;height:34px;display:block;margin:0 auto 10px}
.industry + .industry::before{content:"";position:absolute;left:-19px;top:50px;width:12px;height:12px;border-radius:50%;background:#fff}

/* testimonials */
.testimonial-row{position:absolute;top:2778px;left:198px;display:flex;gap:26px}
.testimonial{width:250px;height:232px;background:#fff;box-shadow:0 3px 14px rgba(20,30,50,.12);padding:22px 22px}
.testimonial .quote{font-family:"Montserrat",sans-serif;font-size:38px;font-weight:800;color:var(--blue);line-height:.6;height:24px}
.testimonial p{font-size:11px;line-height:1.6;color:var(--muted)}
.reviewer{display:flex;align-items:center;gap:10px;margin-top:16px}
.reviewer .dot{width:26px;height:26px;border-radius:50%;background:#d7dde6}
.stars{color:#f3b01b;font-size:11px;letter-spacing:1px}
.reviewer strong{display:block;font-family:"Montserrat",sans-serif;font-size:12px;color:var(--blue)}
.reviewer small{font-size:10px;color:var(--muted)}
.arrow{position:absolute;top:2880px;width:20px;height:20px}

/* contact */
.contact-info{position:absolute;top:3080px;left:186px;width:300px}
.contact-info .eyebrow{font-size:11px;letter-spacing:2px;color:var(--blue);font-family:"Montserrat",sans-serif;font-weight:600;text-transform:uppercase}
.contact-info h2{font-size:30px;font-weight:800;text-transform:uppercase;margin:2px 0 32px}
.contact-info h2 span{color:var(--blue)}
.info-item{display:flex;gap:16px;margin-bottom:28px}
.info-item .icon{width:40px;height:40px;border-radius:50%;background:var(--blue);flex:none;display:flex;align-items:center;justify-content:center}
.info-item .icon svg{width:18px;height:18px}
.info-item h4{font-size:13px;font-weight:700;margin-bottom:3px}
.info-item p{font-size:11px;color:var(--muted);line-height:1.5}
.consult{position:absolute;top:3086px;left:518px;width:610px;height:450px;background:var(--blue);padding:36px 80px;color:#fff;z-index:2}
.consult h3{text-align:center;font-size:24px;font-weight:800;text-transform:uppercase;margin-bottom:26px}
.field{border-bottom:1px solid rgba(255,255,255,.5);font-size:11px;color:#dbe6f6;padding:14px 0 6px}
.field.tall{height:62px}
.submit{position:absolute;right:80px;bottom:36px;background:#fff;color:var(--blue-dark);font-family:"Montserrat",sans-serif;font-weight:700;font-size:11px;padding:11px 22px;border-radius:2px;text-transform:uppercase}

/* footer */
.site-footer{position:absolute;top:3500px;left:0;width:1200px;height:404px}
.footer-bg{position:absolute;top:0;left:0}
.footer-brand{position:absolute;top:148px;left:186px;display:flex;align-items:center;gap:10px;font-family:"Montserrat",sans-serif;font-weight:800;font-size:22px;color:#fff;line-height:1.05}
.footer-brand .brand-mark{background:#fff}
.social{position:absolute;top:224px;left:186px;display:flex;gap:12px}
.social span{width:18px;height:18px;border-radius:50%;background:var(--blue)}
.footer-col{position:absolute;top:104px;color:#fff}
.footer-col h4{font-size:14px;font-weight:700;text-transform:uppercase;margin-bottom:14px}
.footer-col ul{list-style:none}
.footer-col li{font-size:11px;color:#a9b4c5;line-height:2}
.subscribe{display:flex;margin-top:10px}
.subscribe .input{width:120px;height:28px;background:#fff;font-size:10px;color:var(--muted);padding:8px}
.subscribe .go{height:28px;background:var(--blue);font-size:10px;font-weight:700;padding:8px 10px;font-family:"Montserrat",sans-serif}
.copyright{position:absolute;bottom:10px;width:1200px;text-align:center;font-size:10px;color:#7f8a9c;border-top:1px solid rgba(255,255,255,.1);padding-top:10px}
</style>
</head>
<body>

<header class="site-header">
  <div class="brand"><span class="brand-mark"></span><span>TideMill<br>Coatings</span></div>
  <div class="topbar">
    <div class="info"><svg viewBox="0 0 24 24"><path d="M12 2a7 7 0 0 0-7 7c0 5 7 13 7 13s7-8 7-13a7 7 0 0 0-7-7zm0 9.5A2.5 2.5 0 1 1 12 6.5a2.5 2.5 0 0 1 0 5z" fill="#2c66b5"/></svg>Our Location</div>
    <div class="info phone"><svg viewBox="0 0 24 24"><path d="M6.6 10.8a15 15 0 0 0 6.6 6.6l2.2-2.2a1 1 0 0 1 1-.25 11.4 11.4 0 0 0 3.6.57 1 1 0 0 1 1 1V20a1 1 0 0 1-1 1A17 17 0 0 1 3 4a1 1 0 0 1 1-1h3.5a1 1 0 0 1 1 1c0 1.25.2 2.45.57 3.6a1 1 0 0 1-.25 1z" fill="#2c66b5"/></svg>123-456-7890</div>
    <div class="request">Request Services</div>
  </div>
  <nav class="nav">
    <a class="active">Home</a><a>About</a><a>Products</a><a>Applications</a><a>Industries</a><a>Contact Us</a>
  </nav>
</header>

<section class="hero" role="img" aria-label="Worker spray-applying protective coating in an industrial workshop">
  <div class="hero-text">
    <div class="eyebrow">WELCOME TO TIDEMILL COATINGS</div>
    <h1>Delivering Superior Protective Coatings for Automotive and Industrial Applications</h1>
    <a class="btn">Get Started</a>
  </div>
</section>
<svg class="hero-cut" width="1200" height="130" viewBox="0 0 1200 130">
  <polygon points="0,0 600,126 1200,0 1200,130 0,130" fill="#ffffff"/>
  <polyline points="0,4 600,128" stroke="#2c66b5" stroke-width="4" fill="none"/>
  <polyline points="600,128 1200,4" stroke="#2c66b5" stroke-width="4" fill="none"/>
</svg>
<svg class="scroll-down" viewBox="0 0 44 44"><path d="M22 10v22M14 25l8 8 8-8" stroke="#1b2536" stroke-width="2.5" fill="none"/></svg>

<h2 class="section-title" style="top:660px">Our <span>Products</span></h2>
<div class="title-rule" style="top:706px"></div>
<p class="intro" style="top:720px">Lorem ipsum dolor sit amet, consectetur adipiscing elit, sed do eiusmod tempor incididunt ut labore et dolore magna aliqua. Ut enim ad minim veniam, quis nostrud exercitation ullamco laboris.</p>

<div class="product-grid">
  <article class="product-card"><div class="product-media" role="img" aria-label="Red automotive body panel being coated" style="background:linear-gradient(135deg,#c42a22,#7d1510)"></div><span class="product-icon"></span><h3>Lorem Ipsum</h3><p>Lorem ipsum dolor sit amet, consectetur adipiscing elit, sed do eiusmod tempor incididunt ut labore et dolore.</p></article>
  <article class="product-card"><div class="product-media" role="img" aria-label="Technician applying coating in a workshop" style="background:linear-gradient(135deg,#c9b8a4,#7e6b59)"></div><span class="product-icon"></span><h3>Lorem Ipsum</h3><p>Lorem ipsum dolor sit amet, consectetur adipiscing elit, sed do eiusmod tempor incididunt ut labore et dolore.</p></article>
  <article class="product-card"><div class="product-media" role="img" aria-label="Coated metal surface close-up" style="background:linear-gradient(135deg,#8a929c,#4b525b)"></div><span class="product-icon"></span><h3>Lorem Ipsum</h3><p>Lorem ipsum dolor sit amet, consectetur adipiscing elit, sed do eiusmod tempor incididunt ut labore et dolore.</p></article>
  <article class="product-card"><div class="product-media" role="img" aria-label="Steel sheets with protective finish" style="background:linear-gradient(135deg,#b5b9be,#6c7279)"></div><span class="product-icon"></span><h3>Lorem Ipsum</h3><p>Lorem ipsum dolor sit amet, consectetur adipiscing elit, sed do eiusmod tempor incididunt ut labore et dolore.</p></article>
  <article class="product-card"><div class="product-media" role="img" aria-label="Brush applying orange industrial coating" style="background:linear-gradient(135deg,#d97a2b,#5a3a22)"></div><span class="product-icon"></span><h3>Lorem Ipsum</h3><p>Lorem ipsum dolor sit amet, consectetur adipiscing elit, sed do eiusmod tempor incididunt ut labore et dolore.</p></article>
  <article class="product-card"><div class="product-media" role="img" aria-label="Blue coated industrial panel" style="background:linear-gradient(135deg,#3c6fa8,#1d3d63)"></div><span class="product-icon"></span><h3>Lorem Ipsum</h3><p>Lorem ipsum dolor sit amet, consectetur adipiscing elit, sed do eiusmod tempor incididunt ut labore et dolore.</p></article>
</div>
<a class="btn view-all">View All Services</a>

<section class="about">
  <div class="about-media" role="img" aria-label="Stacked coated steel pipes in an industrial warehouse"></div>
  <div class="about-text">
    <div class="eyebrow">About Us</div>
    <h2>Leading the Way in Innovative <span>Protective Coatings</span></h2>
    <p>Lorem ipsum dolor sit amet, consectetur adipiscing elit, sed do eiusmod tempor incididunt ut labore et dolore magna aliqua. Ut enim ad minim veniam, quis nostrud exercitation ullamco laboris nisi ut aliquip ex ea commodo consequat. Duis aute irure dolor in reprehenderit in voluptate velit esse cillum dolore.</p>
    <p>Nulla pariatur. Excepteur sint occaecat cupidatat non proident, sunt in culpa qui officia deserunt mollit anim id est laborum.</p>
    <a class="btn" style="background:var(--blue-dark);margin-top:6px">Read More About Us</a>
  </div>
</section>

<section class="industries">
  <h2>Industries We Serve</h2>
  <div class="rule"></div>
  <p class="lead">Lorem ipsum dolor sit amet, consectetur adipiscing elit, sed do eiusmod tempor incididunt ut labore et dolore.</p>
  <div class="industry-row">
    <div class="industry"><svg viewBox="0 0 34 34"><path d="M5 22l3-8h18l3 8v5H5z M10 27v3M24 27v3" stroke="#2c66b5" stroke-width="2" fill="none"/><circle cx="10" cy="22" r="2" fill="#2c66b5"/><circle cx="24" cy="22" r="2" fill="#2c66b5"/></svg>Automotive<br>Industry</div>
    <div class="industry"><svg viewBox="0 0 34 34"><path d="M17 3v28M4 18l13-5 13 5M11 29l6-3 6 3" stroke="#2c66b5" stroke-width="2" fill="none"/></svg>Aerospace<br>Industry</div>
    <div class="industry"><svg viewBox="0 0 34 34"><circle cx="17" cy="17" r="6" stroke="#2c66b5" stroke-width="2" fill="none"/><path d="M17 4v5M17 25v5M4 17h5M25 17h5M8 8l3.5 3.5M22.5 22.5L26 26M26 8l-3.5 3.5M11.5 22.5L8 26" stroke="#2c66b5" stroke-width="2"/></svg>Manufacturing<br>Industry</div>
    <div class="industry"><svg viewBox="0 0 34 34"><path d="M4 22h26l-4 7H8z M10 22V12h10l4 10 M17 12V5" stroke="#2c66b5" stroke-width="2" fill="none"/></svg>Marine<br>Industry</div>
    <div class="industry"><svg viewBox="0 0 34 34"><path d="M6 30h22M10 30l7-24 7 24M12 22h10M14 15h6" stroke="#2c66b5" stroke-width="2" fill="none"/></svg>Oil and Gas<br>Industry</div>
  </div>
</section>

<h2 class="section-title" style="top:2694px">Our <span>Testimonials</span></h2>
<div class="title-rule" style="top:2740px"></div>
<svg class="arrow" style="left:96px" viewBox="0 0 20 20"><path d="M16 10H4M9 5l-5 5 5 5" stroke="#1b2536" stroke-width="2" fill="none"/></svg>
<svg class="arrow" style="left:1084px" viewBox="0 0 20 20"><path d="M4 10h12M11 5l5 5-5 5" stroke="#1b2536" stroke-width="2" fill="none"/></svg>
<div class="testimonial-row">
  <div class="testimonial"><div class="quote">“</div><p>Lorem ipsum dolor sit amet, consectetur adipiscing elit, sed do eiusmod tempor incididunt ut labore et dolore magna aliqua ut enim ad minim veniam.</p><div class="reviewer"><span class="dot"></span><div><div class="stars">★★★★★</div><strong>Daniel Harper</strong><small>Lorem ipsum</small></div></div></div>
  <div class="testimonial"><div class="quote">“</div><p>Lorem ipsum dolor sit amet, consectetur adipiscing elit, sed do eiusmod tempor incididunt ut labore et dolore magna aliqua ut enim ad minim veniam.</p><div class="reviewer"><span class="dot"></span><div><div class="stars">★★★★★</div><strong>Daniel Harper</strong><small>Lorem ipsum</small></div></div></div>
  <div class="testimonial"><div class="quote">“</div><p>Lorem ipsum dolor sit amet, consectetur adipiscing elit, sed do eiusmod tempor incididunt ut labore et dolore magna aliqua ut enim ad minim veniam.</p><div class="reviewer"><span class="dot"></span><div><div class="stars">★★★★★</div><strong>Daniel Harper</strong><small>Lorem ipsum</small></div></div></div>
</div>

<section class="contact-info">
  <div class="eyebrow">Contact</div>
  <h2>Contact <span>Us</span></h2>
  <div class="info-item"><span class="icon"><svg viewBox="0 0 24 24"><path d="M12 2a7 7 0 0 0-7 7c0 5 7 13 7 13s7-8 7-13a7 7 0 0 0-7-7zm0 9.5A2.5 2.5 0 1 1 12 6.5a2.5 2.5 0 0 1 0 5z" fill="#fff"/></svg></span><div><h4>Location:</h4><p>Address: Lorem ipsum dolor street,<br>Lorem City 00000</p></div></div>
  <div class="info-item"><span class="icon"><svg viewBox="0 0 24 24"><path d="M3 6h18v12H3z M3 6l9 7 9-7" stroke="#fff" stroke-width="2" fill="none"/></svg></span><div><h4>Email Address:</h4><p>info@tidemillcoatings.com</p></div></div>
  <div class="info-item"><span class="icon"><svg viewBox="0 0 24 24"><path d="M6.6 10.8a15 15 0 0 0 6.6 6.6l2.2-2.2a1 1 0 0 1 1-.25 11.4 11.4 0 0 0 3.6.57 1 1 0 0 1 1 1V20a1 1 0 0 1-1 1A17 17 0 0 1 3 4a1 1 0 0 1 1-1h3.5a1 1 0 0 1 1 1c0 1.25.2 2.45.57 3.6a1 1 0 0 1-.25 1z" fill="#fff"/></svg></span><div><h4>Phone Number:</h4><p>123-456-7890</p></div></div>
</section>

<section class="consult">
  <h3>Request a Consultation</h3>
  <div class="field">First Name*</div>
  <div class="field">Last Name*</div>
  <div class="field">Email*</div>
  <div class="field">Subject*</div>
  <div class="field tall">Your message here</div>
  <div class="submit">Submit Now</div>
</section>

<footer class="site-footer">
  <svg class="footer-bg" width="1200" height="404" viewBox="0 0 1200 404">
    <polygon points="0,40 1200,0 1200,404 0,404" fill="#0f1c2f"/>
    <polygon points="0,34 1200,-6 1200,0 0,40" fill="#2c66b5"/>
  </svg>
  <div class="footer-brand"><span class="brand-mark"></span><span>TideMill<br>Coatings</span></div>
  <div class="social"><span></span><span></span><span></span></div>
  <div class="footer-col" style="left:398px"><h4>Quick Links</h4><ul><li>Home</li><li>About</li><li>Products</li><li>Applications</li><li>Industries</li><li>Contact Us</li></ul></div>
  <div class="footer-col" style="left:586px"><h4>Our Services</h4><ul><li>Lorem ipsum dolor</li><li>Lorem ipsum dolor</li><li>Lorem ipsum dolor</li><li>Lorem ipsum dolor</li><li>Lorem ipsum dolor</li><li>Lorem ipsum dolor</li></ul></div>
  <div class="footer-col" style="left:812px"><h4>Contact Info</h4><div class="subscribe"><div class="input">Email Address</div><div class="go">Subscribe Now</div></div></div>
  <div class="copyright">© 2024 TideMill Coatings. All rights reserved.</div>
</footer>

</body>
</html>
```